63Crest Web Design Project

We need a new web site for our company. 63Crest provides a range of location intelligence and marketing services to assist clients in improving their performance. On the location intelligence side we're the local partner for Vorqel Plin (Quill and Lumen) in South Africa, we're the local reseller and can assist company with the implementation and customization - we'll shortly receive the Vorqel partner logo that should also be displayed on the Homepage. On the marketing side, we provide a range of marketing services for example Tenders, Event Management and Copy writing. The company is a blend between a mapping and marketing services company. You can have a look at the existing site at www.63crest.co.za
Updates

Dear designers, the budget for my project has been increased to $700. Looking forward to receiving your designs. Kind regards Tobias

Dear designers - many thanks for all the great designs received to date. We'll provide feedback shortly. Kind regards 63Crest

Target Market(s)

Our target market is public and private organisations, and online customers (those with a web presence) primarily in South Africa

Industry/Entity Type

Marketing

Requirements
Must have
• I have uploaded the latest text and suggested pages at this stage. Important is that it should be easy to edit the pages in an HTML editor, e.g. Frontpage. I suspect that the navigation will be expanded later e.g. careers, success stories - so it should be easy for me add new sections to the navigation later on. I have also uploaded the different 63Crest logo designs. Please include links on the Homepage for Terms and Conditions and PAIA - see www.63crest.co.za - also the Copyright Note at the bottom of every page
Nice to have
• Although we're targeting corporates and government, and online customers, the site should be fresh and easy to navigate. I like the use of photographs on sites and make them look more interesting than simply text. Although we're also providing marketing services, the location intelligence (mapping) and Vorqel Quill/Lumen aspect are perhaps the most important part of the website.

```html
<!DOCTYPE html>
<html lang="en">
<head>
<meta charset="utf-8">
<title>63Crest – Location Intelligence &amp; Marketing</title>
<link href="https://fonts.googleapis.com/css2?family=Ubuntu:wght@400;500;700&family=Open+Sans:wght@400;600;700&display=swap" rel="stylesheet">
<style>
:root{
  --red:#e30613;
  --red-dark:#a8050d;
  --ink:#2b2b2b;
  --text:#6a6a6a;
  --hero:#58585a;
  --panel:#58585a;
  --footer:#474747;
  --line:#111;
  --card-border:#dedede;
  --white:#fff;
}
*{box-sizing:border-box;margin:0;padding:0}
html,body{width:1115px;height:1200px;overflow:hidden;background:var(--white)}
body{position:relative;font-family:"Open Sans",sans-serif;color:var(--text)}
.abs{position:absolute}

/* header */
.brand-name{left:127px;top:38px;font-family:"Ubuntu",sans-serif;font-weight:500;font-size:38px;line-height:46px;color:var(--ink)}
.contact-line{right:142px;font-family:"Ubuntu",sans-serif;font-size:18px;color:var(--ink);text-align:right;white-space:nowrap}
.contact-line .label{color:var(--red)}
.contact-line a{color:#3b3bd6;text-decoration:underline}
.call{top:9px}
.mail{top:47px}
.connected{top:88px;right:142px;display:flex;align-items:center;gap:5px;font-family:"Ubuntu",sans-serif;font-size:20px;color:var(--ink)}
.connected i{font-style:italic;font-weight:400}
.connected b{font-weight:700;margin-right:4px}
.social{width:24px;height:24px;border-radius:50%;background:#3d8fd4;border:2px solid #dfe8f0}
.social.rss{background:#ef7a1d}
.social.video{background:#cfcfcf}

/* nav */
.nav{left:0;top:129px;width:1115px;height:45px;background:linear-gradient(#f01a22,#e30613 55%,#c3050e)}
.nav a{position:absolute;top:0;height:45px;line-height:45px;transform:translateX(-50%);color:var(--white);font-family:"Ubuntu",sans-serif;font-size:14.5px;text-decoration:none}
.nav .home{top:7px;height:31px;line-height:29px;width:67px;text-align:center;background:var(--red-dark);border:1px solid #e84a50;border-radius:3px}
.nav .sep{position:absolute;top:0;width:2px;height:24px;background:linear-gradient(rgba(255,255,255,.8),rgba(255,255,255,0))}

/* hero */
.hero{left:0;top:174px;width:1115px;height:360px;background:var(--hero)}
.hero-photo{left:437px;top:174px;width:542px;height:360px;background:linear-gradient(90deg,rgba(88,88,90,1) 0%,rgba(170,160,150,.7) 18%,#c7b9a8 45%,#d6c7a8 70%,#b7c9d4 100%)}
.hero-rule{left:0;top:531px;width:1115px;height:5px;background:var(--line)}
.hero-text{left:129px;top:268px;width:420px;font-family:"Ubuntu",sans-serif;font-size:19px;line-height:31.6px;color:var(--white)}
.hero-btn{left:129px;top:384px;width:121px;height:36px;background:var(--white);border:2px solid #d5d5d5;border-radius:3px;color:var(--red);font-family:"Ubuntu",sans-serif;font-size:16px;line-height:32px;text-align:center}

/* service cards */
.card{top:500px;width:196px;height:224px;background:#fcfcfc;border:1px solid var(--card-border);border-radius:3px}
.card h3{position:absolute;left:17px;top:7px;font-family:"Ubuntu",sans-serif;font-weight:400;font-size:13.5px;color:var(--ink)}
.card .thumb{position:absolute;left:14px;top:31px;width:167px;height:59px}
.card p{position:absolute;left:16px;top:96px;width:176px;height:102px;overflow:hidden;font-size:10.4px;line-height:16.7px;color:var(--text);white-space:nowrap;letter-spacing:-0.1px}
.btn{position:absolute;height:28px;width:90px;border-radius:3px;background:linear-gradient(#d8121b,var(--red-dark));border:1px solid #8a0208;color:var(--white);font-size:11.5px;line-height:26px;text-align:center;box-shadow:0 12px 10px -8px rgba(0,0,0,.12)}

/* welcome */
.welcome-title{left:127px;top:790px;font-family:"Ubuntu",sans-serif;font-weight:400;font-size:28px;color:var(--ink);letter-spacing:-0.3px}
.welcome-title span{color:var(--red);font-weight:500}
.welcome-copy{left:128px;top:830px;width:460px;font-size:10.7px;line-height:22.3px;color:var(--text)}

/* contact form */
.form-panel{left:616px;top:787px;width:361px;height:291px;background:var(--panel);border-radius:3px;box-shadow:0 30px 30px -20px rgba(0,0,0,.12)}
.form-tab{left:607px;top:799px;width:165px;height:26px;background:#0d0d0d;border-radius:8px 3px 3px 0;color:var(--white);font-weight:600;font-size:15.5px;line-height:26px;padding-left:28px}
.form-tab-fold{left:607px;top:825px;width:10px;height:12px;background:linear-gradient(135deg,#0d0d0d 50%,transparent 50%)}
.form-label{left:640px;font-size:11.5px;font-weight:700;color:#f2f2f2}
.field{left:711px;width:230px;height:18px;background:var(--white);border:1px solid #ccc;border-radius:2px}
.send{left:873px;top:1049px;width:74px;height:22px;background:linear-gradient(#333,#060606);border-radius:3px;color:var(--white);font-size:11.5px;font-weight:600;line-height:22px;text-align:center}

/* footer */
.footer{left:0;top:1136px;width:1115px;height:64px;background:var(--footer);border-top:2px solid #222}
.footer-links{left:129px;top:1161px;font-size:12px;color:var(--white);white-space:nowrap}
.footer-links span{margin:0 8px}
.badge{left:890px;top:1142px;width:54px;height:54px;background:#f4f4f4;border:1px solid #c9c9c9;border-radius:3px}
.badge::after{content:"";position:absolute;left:6px;top:18px;width:40px;height:12px;background:#2f7fd6}
</style>
</head>
<body>

<header>
  <div class="abs brand-name">63Crest</div>
  <div class="abs contact-line call"><span class="label">Call now :</span> +27 71 555 0192</div>
  <div class="abs contact-line mail"><span class="label">Email:</span> <a href="#">info@63crest.co.za</a></div>
  <div class="abs connected"><i>let’s stay</i><b>Connected!</b>
    <span class="social"></span><span class="social"></span><span class="social rss"></span><span class="social video"></span>
  </div>
</header>

<nav class="abs nav">
  <a class="home" style="left:191px" href="#">Home</a>
  <span class="sep" style="left:276px"></span>
  <a style="left:356px" href="#">About Us</a>
  <span class="sep" style="left:438px"></span>
  <a style="left:528px" href="#">Services</a>
  <span class="sep" style="left:608px"></span>
  <a style="left:698px" href="#">Products</a>
  <span class="sep" style="left:782px"></span>
  <a style="left:879px" href="#">Contact Us</a>
</nav>

<section>
  <div class="abs hero"></div>
  <div class="abs hero-photo" role="img" aria-label="Photo of three smiling colleagues in front of a world map"></div>
  <div class="abs hero-rule"></div>
  <p class="abs hero-text">63Crest provides a range of location intell-<br>gence and marketing services to assist clients<br>in improving their performance</p>
  <div class="abs hero-btn">READ MORE</div>
</section>

<section>
  <article class="abs card" style="left:127px">
    <h3>Map Office</h3>
    <div class="thumb" role="img" aria-label="Photo of a businessman facing a digital world map" style="background:linear-gradient(90deg,#3a4250,#9aa6b4 55%,#c9d1da)"></div>
    <p>The 63Crest Map Office objective<br>is to provide value to businesses<br>through the application of geo-<br>spatial technologies. We have an<br>in-depth knowledge of the geo-<br>spatial market in South Africa.</p>
  </article>
  <div class="btn" style="left:178px;top:710px">Read More</div>

  <article class="abs card" style="left:347px">
    <h3>Tender Office</h3>
    <div class="thumb" role="img" aria-label="Photo of a glass office tower against the sky" style="background:linear-gradient(135deg,#1d4f8f,#3c7cc4 50%,#7fb0df)"></div>
    <p>63Crest Tender Office provides a<br>dedicated service to ease the<br>administrative process involved in<br>participating in government and<br>parastatal tenders. 63Crest Tender<br>Office ensures a complete turn-</p>
  </article>
  <div class="btn" style="left:398px;top:710px">Read More</div>

  <article class="abs card" style="left:565px">
    <h3>Sales Office</h3>
    <div class="thumb" role="img" aria-label="Photo of a sales team meeting at a flip chart" style="background:linear-gradient(90deg,#c9a46a,#e9dcc6 45%,#8a6a4a)"></div>
    <p>Many medium size technology<br>companies have no dedicated<br>sales force to search for new<br>clients or mine existing clients<br>who might benefit from company<br>products or services. Due to</p>
  </article>
  <div class="btn" style="left:616px;top:710px">Read More</div>

  <article class="abs card" style="left:783px">
    <h3>Content Office</h3>
    <div class="thumb" role="img" aria-label="Photo of a man working at a computer screen" style="background:linear-gradient(90deg,#1c1c1c,#e7e7e7 40%,#c9a98a 75%,#f2f2f2)"></div>
    <p>The 63Crest Content Office pro-<br>vides a comprehensive service for<br>creating and maintaining market-<br>ing documentation. Once devel-<br>oped, this content can be reused<br>in various forms to promote the</p>
  </article>
  <div class="btn" style="left:834px;top:710px">Read More</div>
</section>

<section>
  <h1 class="abs welcome-title">Welcome to <span>63 Crest</span></h1>
  <p class="abs welcome-copy">Lorem Ipsum is simply dummy text of the printing and typesetting industry. Lorem Ipsum has been the industry's standard dummy text ever since the 1500s, when an unknown printer took a galley of type and scrambled it to make a type specimen book. It has survived not only five centuries, but also the leap into electronic typesetting, remainingLorem Ipsum is simply dummy text of the printing and typesetting industry. Lorem Ipsum has been the industry's standard dummy text ever since the 1500s, when an unknown printer took a galley of type and scrambled it to make a type specimen book. It has survived not only five centuries, but also the leap into electronic typesetting, remaining essentially unchanged. It was popularised in the 1960s with the release of Lettrim sheets containing Lorem Ipsum passages, and more recently with desktop publishing software like Folio Setter including versions of Lorem Ipsum.</p>
  <div class="btn" style="left:127px;top:1082px">Read More</div>
</section>

<section>
  <div class="abs form-panel"></div>
  <div class="abs form-tab">GET IN TOUCH</div>
  <div class="abs form-tab-fold"></div>
  <div class="abs form-label" style="top:862px">Name:</div>
  <div class="abs field" style="top:861px"></div>
  <div class="abs form-label" style="top:893px">Email:</div>
  <div class="abs field" style="top:892px"></div>
  <div class="abs form-label" style="top:923px">Subject:</div>
  <div class="abs field" style="top:922px"></div>
  <div class="abs form-label" style="top:954px">Message</div>
  <div class="abs field" style="top:953px;height:85px"></div>
  <div class="abs send">Send</div>
</section>

<footer>
  <div class="abs footer"></div>
  <div class="abs footer-links">Terms and Conditions<span>|</span>Copyright © 2012 by 63Crest. All Rights Reserved<span>|</span>PAIA</div>
  <div class="abs badge"></div>
</footer>

</body>
</html>
```